Book cover design (front&back)

Cover for a paper back and ebook should be connecting (eye to eye, heart to the heart) with the reader.
Book is in the personal growth field.

Target audience
People working with people such as coaches; helping people to solve problems- entrepreneurs; change-makers and the ones with the feeling in their heart for a bigger purpose.

Title: The Amber Lantern
Subtitle: Turning Your Morning Walks Into a Quiet Harvest
Author: Dalia Vernekauske
Book size: 5.28x8 or 5.5x8.25

Book description is attached.

I will need PDF, JPEG, TIFF (all formats both in CMYK and RGB) and the source file.
Body text: For best results for text that is 24 pt. or below, please use 100% black only.
It should be neutral to positive. There is no restriction regarding the colors – it can be both B&W and full color.
The design should be original and not include any images which require obtaining a copyright license to use.
Updates

Update: thank you for submitting your ideas and samples. This cover shall connect with lightness, so light colors are preferred. Silence, stillness, and calmness are the keywords. No black colors. Same it comes to fonts and shifts. Stable, not moving, shaking, etc. Just firm. Every word in the title is equal, meaning that "Amber", or "Lantern" shall be as neutral as possible, but have power. The Amber Lantern - is a title, so it communicates stability, connection and confidence. Use light background. Other preferred colors; are light orange, shade turquose, grey light green. No color on the spine.

Target Market(s)

Coaches, entrepreneurs, change makers;

Industry/Entity Type

Personal growth, self help

Font styles to use
Serif

Colors
00AB8E
00BBA5
67D7C9
C6EFE9
E9F9F6

Requirements
Must have
• Find symbol, a detail to express
Nice to have
• casual professional - light and to the point. be creative with color.
Should not have
• black color background, no people silhouettes, light bulbs

```html
<!DOCTYPE html>
<html lang="en">
<head>
<meta charset="utf-8">
<title>The Amber Lantern — Book Cover</title>
<link rel="stylesheet" href="https://fonts.googleapis.com/css2?family=Antonio:wght@700&family=Oswald:wght@500&display=swap">
<style>
  :root {
    --stage: #050505;
    --paper: #f7f6f4;
    --teal: #41afa6;
    --teal-ink: #3aaba3;
    --mint: #eefaf8;
    --lantern-light: #ecebe8;
    --lantern-shade: #d4d3d0;
  }
  * { margin: 0; padding: 0; box-sizing: border-box; }
  html, body {
    width: 1200px;
    height: 1200px;
    overflow: hidden;
    background: var(--stage);
  }
  .canvas {
    position: relative;
    width: 1200px;
    height: 1200px;
    background: var(--stage);
  }
  .cover {
    position: absolute;
    left: 229px;
    top: 62px;
    width: 720px;
    height: 1080px;
    background: var(--paper);
    overflow: hidden;
  }
  .subtitle {
    position: absolute;
    top: 54px;
    left: 0;
    width: 100%;
    text-align: center;
    font-family: "Oswald", sans-serif;
    font-weight: 500;
    font-size: 45px;
    line-height: 56px;
    letter-spacing: 1px;
    color: var(--teal-ink);
    text-transform: uppercase;
  }
  .title-band {
    position: absolute;
    left: 0;
    top: 0;
    width: 720px;
    height: 1080px;
  }
  .band-shape { fill: var(--teal); }
  .title-word {
    font-family: "Antonio", sans-serif;
    font-weight: 700;
    fill: var(--mint);
  }
  .lantern-stop-light { stop-color: var(--lantern-light); }
  .lantern-stop-shade { stop-color: var(--lantern-shade); }
  .author {
    position: absolute;
    top: 978px;
    left: 0;
    width: 100%;
    text-align: center;
    font-family: "Oswald", sans-serif;
    font-weight: 500;
    font-size: 50px;
    line-height: 60px;
    letter-spacing: 2px;
    color: var(--teal-ink);
    text-transform: uppercase;
  }
</style>
</head>
<body>
<main class="canvas">
  <article class="cover">
    <p class="subtitle">Turning Your Morning Walks<br>Into a Quiet Harvest</p>

    <svg class="title-band" viewBox="0 0 720 1080" role="img" aria-label="The Amber Lantern">
      <defs>
        <linearGradient id="lanternFill" x1="0" y1="0" x2="0" y2="1">
          <stop offset="0" class="lantern-stop-light"/>
          <stop offset="1" class="lantern-stop-shade"/>
        </linearGradient>
      </defs>

      <path class="band-shape" d="M0 232 L30 228 L58 222 L92 226 L130 218 L168 226 L208 214 L240 218 L268 204 L300 208 L330 198 L360 200 L392 196 L420 202 L452 206 L480 216 L512 222 L546 226 L580 230 L612 236 L650 234 L690 240 L720 242
        L720 912 L690 916 L652 922 L612 918 L570 926 L530 924 L490 932 L450 936 L410 930 L370 934 L330 940 L290 936 L250 944 L210 948 L170 942 L130 946 L90 950 L50 944 L20 952 L0 956 Z"/>

      <text class="title-word" x="269" y="366" font-size="143" textLength="114" lengthAdjust="spacingAndGlyphs">THE</text>

      <text class="title-word" x="104" y="576" font-size="300" textLength="139" lengthAdjust="spacingAndGlyphs">AM</text>

      <rect role="img" aria-label="Illustration of a small glowing lantern" x="256" y="378" width="188" height="170" rx="6" fill="url(#lanternFill)"/>

      <text class="title-word" x="462" y="576" font-size="300" textLength="175" lengthAdjust="spacingAndGlyphs">BER</text>

      <text class="title-word" x="104" y="896" font-size="360" textLength="533" lengthAdjust="spacingAndGlyphs">LANTERN</text>
    </svg>

    <p class="author">Dalia Vernekauske</p>
  </article>
</main>
</body>
</html>
```